(The Splash Lady) Cleaning swimming pool's & Spa's weekly for a monthly Rate

Name of company is (KTR Pool & Spa Cleaning) Lic.# 718365 __ KTR are initials for Kate Tessa Rowan, a female owner, nick name for her and company is (The Splash Lady) we would like to see Company and Nick name plus Lic. # on post card along with contact # 951-555-0148 call or Text and e-mail address(k_tbluewave@examplemail.net) No business Address posted being its our home address, also post an incentive to use our service as follows (50% off First Month of Maintenance, Very Reasonable Rate's !! ) incentive written in the middle of a picture of a Gorgeous swimming pool and to one side of picture is the silhouette profile of a woman with or without holding a pole with a cleaning net at end of pole, color of card maybe different shades of blue or just all blue. what we provide is a weekly cleaning maintenance service on in ground swimming pool's & Spa's, Thank you, Kate

Target Market(s)

Home Owners with in ground swimming pools

Industry/Entity Type

It Company

Font styles to use
Serif
Decorative
Script

Requirements
Must have
• Silhouette outline profile design or picture of a woman next to a elegant swimming pool, colors of outline woman are to be contrast color like a pink or light grey against a blue background postcard
Nice to have
• nick name(The Splash Lady) and company name (KTR Pool & Spa Cleaning) on postcard, A small logo of a bar and shield stamp on one corner of card, KTR should read on bar, upper half of shield CLEAN should read and bottom half P00LS should read. uploaded files show bar and shield and possible picture of woman
Should not have
• None

```html
<!DOCTYPE html>
<html lang="en">
<head>
<meta charset="utf-8">
<title>KTR Pool &amp; Spa Cleaning – Postcard</title>
<link rel="stylesheet" href="https://fonts.googleapis.com/css2?family=Oswald:wght@400;500&family=Kaushan+Script&family=Roboto+Condensed:wght@400;500&family=Ubuntu:wght@500;700&display=swap">
<style>
  :root{
    --page:#eef1f4;
    --navy:#0e4f80;
    --deep:#0c568c;
    --mid:#1d8fd0;
    --sky:#5cc6f0;
    --light:#9ee0ff;
    --ink:#1a5a8a;
    --white:#ffffff;
    --rule:#c4c8cc;
  }
  *{margin:0;padding:0;box-sizing:border-box}
  html,body{width:896px;height:1200px;overflow:hidden;background:var(--page)}
  .card-slot{position:absolute;width:620px;height:480px;box-shadow:0 4px 14px rgba(0,0,0,.25);overflow:hidden}
  .card-slot.front{left:60px;top:80px}
  .card-slot.back{left:216px;top:620px}
  .card{position:absolute;left:0;top:0;width:671px;height:520px;transform:scale(.924);transform-origin:0 0;overflow:hidden}
  .abs{position:absolute}
  .caps{font-family:"Oswald",sans-serif;font-weight:500;color:var(--ink);text-transform:uppercase}
  .script{font-family:"Kaushan Script",cursive;color:var(--navy)}
  .cond{font-family:"Roboto Condensed",sans-serif;font-weight:500}
  .num{font-family:"Ubuntu",sans-serif;font-weight:700}
  .brand-mark{display:flex;align-items:center;gap:10px;font-family:"Oswald",sans-serif;font-weight:500;color:var(--deep)}
  .brand-mark .dot{background:var(--deep)}

  /* front */
  .front .pool-photo{left:0;top:60px;width:671px;height:400px;
    background:linear-gradient(180deg,#3d4a38 0%,#6b5a3e 35%,#7a8b86 55%,#6fbfe0 72%,#3f8fc4 100%)}
  .front .silhouette{left:10px;top:128px;width:150px;height:276px;background:#b9bcc0;border-radius:60px 60px 8px 8px;opacity:.92}
  .front .title{left:30px;top:18px;font-size:26px;letter-spacing:3.2px}
  .front .nick{left:100px;top:52px;font-size:33px}
  .front .brand-mark{left:440px;top:70px;font-size:58px;letter-spacing:6px}
  .front .brand-mark .dot{width:26px;height:26px}
  .front .lic{left:571px;top:174px;font-size:13px;color:var(--white);font-family:"Ubuntu",sans-serif;font-weight:500}
  .front .offer{left:180px;top:148px;color:var(--white);font-family:"Ubuntu",sans-serif;font-weight:700;font-size:86px;letter-spacing:-3px;line-height:1;text-shadow:0 2px 4px rgba(0,0,0,.45)}
  .front .offer small{font-size:50px;letter-spacing:-1px}
  .front .offer-line{color:var(--white);font-family:"Oswald",sans-serif;font-weight:500;font-size:21px;text-shadow:0 1px 3px rgba(0,0,0,.6);transform:scaleX(.85);transform-origin:0 0;white-space:nowrap}
  .front .offer-line.one{left:184px;top:240px}
  .front .offer-line.two{left:200px;top:272px}
  .front .services{left:26px;top:440px;display:flex;gap:10px;color:var(--white);font-size:14px;letter-spacing:1px;line-height:20px;text-transform:uppercase}
  .front .services svg{flex:none;margin-top:-2px}
  .front .contact{right:18px;top:436px;width:252px;color:var(--white);white-space:nowrap}
  .front .contact .ask{font-size:14px;color:var(--light);letter-spacing:.4px;text-align:right}
  .front .contact .row{display:flex;align-items:center;justify-content:flex-end;gap:12px;margin-top:2px}
  .front .contact .phone{font-size:27px}
  .front .contact .email{font-size:15px;color:var(--light);letter-spacing:.2px;text-align:right;margin-top:1px}

  /* back */
  .back .card{background:linear-gradient(90deg,#f4fbfe 0%,#ffffff 50%,#e4f3fb 100%)}
  .back .brand-mark{left:46px;top:30px;font-size:40px;letter-spacing:4px}
  .back .brand-mark .dot{width:18px;height:18px}
  .back .nick{left:170px;top:40px;font-size:32px}
  .back .title{left:60px;top:96px;font-size:27px;letter-spacing:.5px}
  .back .lic{left:142px;top:138px;font-size:17px;color:var(--navy);font-family:"Ubuntu",sans-serif;font-weight:500;letter-spacing:1px}
  .back .ask{left:50px;top:180px;font-size:19px;color:var(--mid);letter-spacing:.4px}
  .back .phone-row{left:50px;top:206px;display:flex;align-items:center;gap:16px}
  .back .phone{font-size:28px;color:var(--mid)}
  .back .email{left:112px;top:242px;font-size:18px;color:var(--mid);letter-spacing:.3px}
  .back .portrait{left:42px;top:320px;width:150px;height:150px;border-radius:50%;border:5px solid var(--sky);
    background:linear-gradient(160deg,#6f8a52 0%,#8aa35e 50%,#e8a6b4 100%)}
  .back .splash{left:196px;top:318px;width:126px;height:150px;border-radius:50% 50% 40% 60%;background:linear-gradient(160deg,#5cc6f0,#1d8fd0)}
  .back .stamp{left:546px;top:24px;width:96px;height:81px;border:1.5px solid var(--rule)}
  .back .address-line{left:403px;width:244px;height:2px;background:var(--rule)}
</style>
</head>
<body>

<!-- FRONT -->
<div class="card-slot front">
  <div class="card">
    <div class="abs pool-photo" role="img" aria-label="Photo of an elegant modern home with a lit swimming pool and wooden bench at dusk"></div>
    <div class="abs silhouette" role="img" aria-label="Light grey silhouette of a woman in a hat holding a pool cleaning pole"></div>

    <svg class="abs" style="left:0;top:0" width="671" height="520" viewBox="0 0 671 520" aria-hidden="true">
      <defs>
        <linearGradient id="bannerFill" x1="0" y1="0" x2="1" y2="0">
          <stop offset="0" stop-color="#dff3fc"/><stop offset=".7" stop-color="#c4e9f9"/><stop offset="1" stop-color="#5cc6f0"/>
        </linearGradient>
      </defs>
      <path d="M0 0H671V110C600 105 520 96 460 92C380 88 300 108 220 118C140 126 60 110 0 84Z" fill="url(#bannerFill)"/>
      <path d="M0 86C70 112 150 124 230 118C280 114 320 104 360 92C320 110 280 122 220 126C140 130 60 116 0 96Z" fill="#5cc6f0"/>
      <path d="M0 420C120 380 300 376 440 430C380 406 300 396 220 396C130 396 60 406 0 426Z" fill="#1d8fd0"/>
      <path d="M0 428C120 392 300 392 450 436C540 460 620 440 671 420V520H0Z" fill="#0e4f80"/>
    </svg>

    <div class="abs caps title">KTR Pool &amp; Spa Cleaning</div>
    <div class="abs script nick">The Splash Lady</div>
    <div class="abs brand-mark"><span class="dot"></span>KTR</div>
    <div class="abs lic">Lic.#718365</div>

    <div class="abs offer">50%<small> off</small></div>
    <div class="abs offer-line one">First Month of Maintenance,</div>
    <div class="abs offer-line two">Very Reasonable Rate's !!</div>

    <div class="abs services cond">
      <svg width="26" height="26" viewBox="0 0 26 26"><circle cx="13" cy="13" r="12" fill="#fff"/><path d="M10 7l6 6-6 6" fill="none" stroke="#0e4f80" stroke-width="3"/></svg>
      <div>We provide&nbsp; weekly cleaning<br>maintenance service on in ground<br>swimming pool's &amp; spa's</div>
    </div>

    <div class="abs contact">
      <div class="ask cond">Call us now for a free estimate!</div>
      <div class="row">
        <svg width="40" height="36" viewBox="0 0 44 40"><path d="M4 14C4 6 40 6 40 14V18H31V13H13V18H4Z" fill="#fff"/><path d="M8 22H36L40 38H4Z" fill="#fff"/><circle cx="22" cy="30" r="5" fill="#0e4f80"/></svg>
        <span class="num phone">951-555-0148</span>
      </div>
      <div class="email cond">k_tbluewave@examplemail.net</div>
    </div>
  </div>
</div>

<!-- BACK -->
<div class="card-slot back">
  <div class="card">
    <div class="abs brand-mark"><span class="dot"></span>KTR</div>
    <div class="abs script nick">The Splash Lady</div>
    <div class="abs caps title">KTR Pool &amp; Spa Cleaning</div>

    <svg class="abs" style="left:0;top:0" width="671" height="520" viewBox="0 0 671 520" aria-hidden="true">
      <path d="M0 116C60 150 160 160 240 154C290 150 330 144 360 140C320 156 270 166 210 170C130 174 50 160 0 132Z" fill="#5cc6f0"/>
      <path d="M0 470C200 450 420 440 671 460V520H0Z" fill="#1d8fd0"/>
      <path d="M0 478C220 458 440 462 671 474V520H0Z" fill="#0e4f80"/>
    </svg>

    <div class="abs lic">Lic.# 718365</div>
    <div class="abs ask cond">Call us now for a free estimate!</div>
    <div class="abs phone-row">
      <svg width="42" height="38" viewBox="0 0 44 40"><path d="M4 14C4 6 40 6 40 14V18H31V13H13V18H4Z" fill="#1d8fd0"/><path d="M8 22H36L40 38H4Z" fill="#1d8fd0"/><circle cx="22" cy="30" r="5" fill="#fff"/></svg>
      <span class="num phone">951-555-0148</span>
    </div>
    <div class="abs email cond">k_tbluewave@examplemail.net</div>

    <div class="abs portrait" role="img" aria-label="Circular portrait photo of the owner outdoors on a golf course"></div>
    <div class="abs splash" role="img" aria-label="Blue water splash with droplets"></div>

    <div class="abs stamp"></div>
    <div class="abs address-line" style="top:177px"></div>
    <div class="abs address-line" style="top:205px"></div>
    <div class="abs address-line" style="top:233px"></div>
    <div class="abs address-line" style="top:261px"></div>
    <div class="abs address-line" style="top:289px"></div>
  </div>
</div>

</body>
</html>
```